Tots at Play

We need a logo and graphich design for a one page text for our Tots @play program, it would nened to match or be inspired from our corporate indentity which can be seen at www.halvora-partners.com

Dear XXX
BRT is proud to launch its first ever TOTS @ PLAY day! We invite you and your child(ren) to join us on this special day, and strengthen the connection between education and work, and your relationship between parent and child(ren).

Who? All children, all ages
Where? BRT offices
When? January 29th, from 13h – 17h

Tots @ Play is the perfect time to start shaping your children’s future through education and experience at BRT with a program tailored to target each age group. There will be group activities and sessions, as well as one on one time for parents and their children.
We are excited to work together with you and your children to create a true sense of community, and celebrate the opportunities and possibilities for the next generation. It’s a day to share your passion and know-how and show what happens when you are at work. We will show children the value of education and help them discover the power and potential of a balanced work and family life. We would like to give you and your children an opportunity to express their future goals and dreams and help begin together the steps towards achieving these through the follow up with Tots @ Quest. BRT is developing a multi-program to enable parents and children to realize the future they dream of.
We look forward to seeing you @ Work!

Industry/Entity Type

Education

```html
<!DOCTYPE html>
<html lang="en">
<head>
<meta charset="utf-8">
<title>Tots @ Play – Stationery</title>
<link rel="stylesheet" href="https://fonts.googleapis.com/css2?family=Open+Sans:wght@400;600;700&family=Tinos&display=swap">
<style>
  :root {
    --backdrop: #f04a80;
    --brand-pink: #d81e6c;
    --brand-purple: #5b2a86;
    --dash-purple: #7a2bd6;
    --swirl-orange: #f7a21b;
    --swirl-blue: #2aa6dc;
    --ink: #111111;
    --card-cream: #f7f6ec;
    --paper: #ffffff;
  }
  * { box-sizing: border-box; margin: 0; padding: 0; }
  html, body { width: 948px; height: 1200px; overflow: hidden; }
  body {
    background: var(--backdrop);
    font-family: "Open Sans", Arial, sans-serif;
    color: var(--ink);
    position: relative;
  }

  .brand-name {
    font-family: "Open Sans", Arial, sans-serif;
    font-weight: 600;
    color: var(--brand-pink);
    line-height: 1;
    letter-spacing: 1px;
    position: absolute;
  }

  .corner-swirl {
    position: absolute;
    right: 0;
    bottom: 0;
    border-radius: 60% 55% 0 0 / 100% 100% 0 0;
    background: linear-gradient(90deg, var(--brand-pink) 0%, var(--brand-pink) 30%, var(--swirl-orange) 50%, var(--brand-purple) 75%, var(--swirl-blue) 100%);
  }

  .guide-ring { position: absolute; pointer-events: none; overflow: visible; }

  /* Business card */
  .business-card {
    position: absolute;
    left: 62.6px; top: 39.8px;
    width: 817px; height: 391.5px;
    background: radial-gradient(ellipse at 40% 40%, #fbfaf3 0%, var(--card-cream) 60%, #eeecd9 100%);
    overflow: hidden;
  }
  .business-card .brand-name { left: 30px; top: 34px; font-size: 58px; }
  .floral-field {
    position: absolute;
    right: 0; top: 0;
    width: 230px; height: 300px;
    background: radial-gradient(ellipse at 70% 40%, rgba(230,228,205,0.9) 0%, rgba(240,238,222,0.4) 60%, rgba(247,246,236,0) 100%);
  }
  .business-card .corner-swirl { width: 300px; height: 150px; }
  .contact-block {
    position: absolute;
    left: 316px; top: 68px;
    width: 200px;
    text-align: center;
  }
  .person-name { font-weight: 700; font-size: 16px; letter-spacing: 0.2px; }
  .person-role { font-size: 14px; margin-top: 1px; }
  .address-lines { margin-top: 14px; font-size: 11.5px; line-height: 18px; }
  .address-lines .small { font-size: 11px; }

  /* Lanyard + badge */
  .lanyard { position: absolute; left: 0; top: 0; width: 948px; height: 1200px; pointer-events: none; }
  .id-badge {
    position: absolute;
    left: 81.5px; top: 502px;
    width: 209px; height: 322px;
    background: var(--paper);
    border-radius: 16px;
    overflow: hidden;
  }
  .id-badge .brand-name { left: 8px; top: 18px; font-size: 32px; }
  .badge-details {
    position: absolute;
    left: 0; top: 112px; width: 100%;
    text-align: center;
  }
  .badge-details .person-name { font-size: 17px; }
  .badge-details .person-role { font-size: 14.5px; }
  .badge-tel { margin-top: 15px; font-size: 12.5px; }
  .badge-web { margin-top: 12px; font-size: 8.5px; line-height: 15px; }
  .id-badge .corner-swirl { width: 160px; height: 62px; }
  .badge-eyelet {
    position: absolute;
    left: 178px; top: 478px;
    width: 12px; height: 14px;
    border: 3px solid #9a9a9a;
    border-radius: 6px;
  }

  /* Letterhead */
  .letterhead {
    position: absolute;
    left: 405px; top: 490px;
    width: 475px; height: 671px;
    background: var(--paper);
    overflow: hidden;
  }
  .letterhead .brand-name { left: 18px; top: 28px; font-size: 42px; }
  .event-facts {
    position: absolute;
    left: 282px; top: 24px;
    font-family: "Tinos", "Times New Roman", serif;
    font-size: 11px;
    line-height: 12.5px;
  }
  .event-facts dt { display: inline; color: var(--brand-pink); }
  .event-facts dd { display: inline; }
  .letterhead .corner-swirl { width: 200px; height: 105px; }
</style>
</head>
<body>

  <section class="business-card">
    <svg class="guide-ring" width="817" height="392" viewBox="0 0 817 392" style="left:0;top:0">
      <circle cx="122" cy="69" r="124" fill="none" stroke="var(--brand-pink)" stroke-width="1.5" stroke-dasharray="2 3"/>
      <circle cx="122" cy="69" r="112" fill="none" stroke="var(--brand-purple)" stroke-width="1" stroke-dasharray="6 4"/>
    </svg>
    <div class="brand-name">BRT</div>
    <div class="floral-field" role="img" aria-label="Faint floral leaf pattern"></div>
    <div class="contact-block">
      <div class="person-name">YOUR NAME</div>
      <div class="person-role">Your Position</div>
      <div class="address-lines">
        <div>Address Line 1, Address Line 2</div>
        <div>Address Line 3, Address Line 4</div>
        <div>Tel : +00 0000 0000</div>
        <div>Fax : +00 0000 0000</div>
        <div>Email: <span class="small">mara.lindqvist@halvora-partners.com</span></div>
        <div>Website: <span class="small">http://www.halvora-partners.com</span></div>
      </div>
    </div>
    <div class="corner-swirl" role="img" aria-label="Colourful paisley swirl ornament in pink, orange, purple and blue"></div>
  </section>

  <svg class="lanyard" viewBox="0 0 948 1200">
    <defs>
      <linearGradient id="strapTone" x1="0" y1="0" x2="0" y2="1">
        <stop offset="0" stop-color="var(--brand-pink)"/>
        <stop offset="1" stop-color="var(--brand-purple)"/>
      </linearGradient>
    </defs>
    <path d="M183 485 C 260 470, 330 520, 345 640 C 355 720, 345 790, 322 790 C 296 790, 300 720, 305 680 C 312 600, 282 530, 186 492"
          fill="none" stroke="url(#strapTone)" stroke-width="6" stroke-linecap="round"/>
  </svg>

  <section class="id-badge">
    <svg class="guide-ring" width="209" height="322" viewBox="0 0 209 322" style="left:0;top:0">
      <circle cx="10" cy="-10" r="96" fill="none" stroke="var(--brand-pink)" stroke-width="1.2" stroke-dasharray="2 3"/>
      <circle cx="10" cy="-10" r="88" fill="none" stroke="var(--brand-purple)" stroke-width="0.8" stroke-dasharray="5 3"/>
    </svg>
    <div class="brand-name">BRT</div>
    <div class="badge-details">
      <div class="person-name">YOUR NAME</div>
      <div class="person-role">Your Position</div>
      <div class="badge-tel">Tel : +00 0000 0000</div>
      <div class="badge-web">
        <div>Email: mara.lindqvist@halvora-partners.com</div>
        <div>Website: http://www.halvora-partners.com</div>
      </div>
    </div>
    <div class="corner-swirl" role="img" aria-label="Colourful paisley swirl ornament"></div>
  </section>
  <div class="badge-eyelet"></div>

  <section class="letterhead">
    <svg class="guide-ring" width="475" height="671" viewBox="0 0 475 671" style="left:0;top:0">
      <circle cx="10" cy="-60" r="190" fill="none" stroke="var(--brand-pink)" stroke-width="3" stroke-dasharray="3 4"/>
      <circle cx="10" cy="-60" r="178" fill="none" stroke="var(--dash-purple)" stroke-width="2" stroke-dasharray="10 6"/>
    </svg>
    <div class="brand-name">BRT</div>
    <dl class="event-facts">
      <div><dt>Who:</dt> <dd>All children, all ages</dd></div>
      <div><dt>Where:</dt> <dd>BRT offices</dd></div>
      <div><dt>When:</dt> <dd>January 29th, from 13h – 17h</dd></div>
    </dl>
    <div class="corner-swirl" role="img" aria-label="Colourful paisley swirl ornament"></div>
  </section>

</body>
</html>
```